Landing Page für Freelancer im Bereich der Informationstechnik
Zielgruppe
Ich bin Experte für Informationstechnik, Unified Communications, Beratung, Management sowie Projekte aller Art.
Mit meiner WOLKENTOR GmbH bin ich als (einzelner) Freelancer für mittelständische Unternehmen und Konzerne in verschiedensten Projekten tätig.
Mein Motto lautet 'Mit Präzision und langjähriger Erfahrung immer alles im Griff!'
Aufgabenstellung
Die aktuell existierende Internet-Präsenz unter wolkentor-web.de beinhaltet aktuell nur eine minimalistische statische Seite sowie das Impressum, ohne jegliche dynamische Inhalte.
DABEI SOLL ES BLEIBEN. Auch die Inhalte sollen unverändert übernommen werden.
Lediglich soll jetzt eine Anlehnung an das zwischenzeitlich vorhandene Logo vorgenommen werden, welches ich mitliefere.
Es geht mir insgesamt nur darum, ein professionelleres Auftreten zu haben, WENN sich denn mal jemand auf die Seite verirrt.
Das Aussehen soll daher modern und dynamisch sein.
ZUSAMMENFASSUNG: Inhalte bleiben 1:1, grafische Anpassung an Logo gewünscht.
Technisch: Statisch, kein Content-Management. Lohnt sich hier nicht.
SEHR WICHTIG: Ich möchte gerne, dass die Lieferung bereits als HTML (und NICHT NUR ALS GRAFIK) erfolgt, ggf. stelle ich auch kurz den FTP-Zugang.
Insgesamt möchte ich gar keine große Sache draus machen.
Viele Anpassungsrunden wird es voraussichtlich nicht geben.
Zeitlich ist dies hier ein sehr kleines Projekt - Erweiterungen kommen später.

```html
<!DOCTYPE html>
<html lang="de">
<head>
<meta charset="utf-8">
<title>Matthias Konrad Berger – WOLKENTOR GmbH</title>
<link rel="stylesheet" href="https://fonts.googleapis.com/css2?family=Russo+One&family=Open+Sans:ital,wght@0,400;0,600;0,700;1,400;1,600&display=swap">
<style>
  :root {
    --accent: #4aa4c0;
    --card: #d9d9d9;
    --text: #444a4d;
    --ink: #111;
    --bg: #ffffff;
    --logo-bg: #f9fbfc;
  }
  * { box-sizing: border-box; margin: 0; padding: 0; }
  html, body { width: 1200px; height: 709px; overflow: hidden; background: var(--bg); }
  body { position: relative; font-family: "Open Sans", Arial, sans-serif; color: var(--text); }

  .name {
    position: absolute; left: 20px; top: 86px;
    font-family: "Russo One", "Arial Black", sans-serif;
    font-weight: 400; font-size: 57px; line-height: 1;
    color: var(--accent); letter-spacing: 0.5px; white-space: nowrap;
  }
  .degrees {
    position: absolute; left: 22px; top: 180px;
    font-size: 22px; line-height: 29px; color: var(--text);
  }

  .brand {
    position: absolute; left: 969px; top: 47px; width: 143px; height: 145px;
    background: var(--logo-bg);
    display: flex; flex-direction: column; align-items: center; justify-content: center; gap: 8px;
  }
  .brand-dot { width: 22px; height: 22px; border-radius: 50%; background: var(--accent); }
  .brand-name { font-size: 12px; font-weight: 600; color: var(--accent); letter-spacing: 0.5px; }

  .card {
    position: absolute; background: var(--card); border-radius: 6px;
    text-align: center;
  }
  .card::before {
    content: ""; position: absolute; top: -14px; right: 0; height: 16px; width: 70%;
    background: var(--card); border-radius: 6px 6px 0 0;
    clip-path: polygon(8px 0, 100% 0, 100% 100%, 0 100%);
  }
  .card.small::before { width: 60%; top: -10px; height: 12px; }
  .card-label {
    position: absolute; left: 0; right: 0;
    font-size: 15px; font-weight: 600; color: var(--ink);
  }
  .card.big { width: 265px; height: 179px; top: 306px; }
  .card.big .card-label { top: 38px; }
  .card.big svg { position: absolute; left: 50%; top: 81px; transform: translateX(-50%); }
  .card.small { width: 171px; height: 149px; top: 516px; }
  .card.small .card-label { top: 22px; }
  .card.small svg { position: absolute; left: 50%; top: 72px; transform: translateX(-50%); }

  .motto {
    position: absolute; left: 600px; width: 586px; top: 348px;
    text-align: center; font-style: italic; font-weight: 400;
    font-size: 23.5px; line-height: 31px; color: var(--accent);
  }
  .contact {
    position: absolute; left: 632px; top: 499px; width: 530px;
    font-size: 14.5px; line-height: 21px; color: var(--text);
  }
  .contact p + p { margin-top: 21px; }
  .contact strong { font-weight: 700; color: #333; }
  .legal {
    position: absolute; left: 632px; top: 644px;
    font-size: 14.5px; color: var(--text); text-decoration: underline;
  }
</style>
</head>
<body>
  <h1 class="name">MATTHIAS KONRAD BERGER</h1>
  <div class="degrees">Diplom-Informatiker (FH)<br>Master of Science in Electronic Business</div>

  <div class="brand">
    <span class="brand-dot"></span>
    <span class="brand-name">WOLKENTOR GmbH</span>
  </div>

  <div class="card big" style="left:20px">
    <div class="card-label">Experte für Informationstechnik</div>
    <svg width="66" height="72" viewBox="0 0 66 72">
      <polygon points="33,2 64,19 64,53 33,70 2,53 2,19" fill="var(--accent)"/>
      <text x="33" y="46" text-anchor="middle" font-family="Russo One, sans-serif" font-size="26" fill="#d9d9d9">PRO</text>
    </svg>
  </div>

  <div class="card big" style="left:319px">
    <div class="card-label">Unified Communications</div>
    <svg width="72" height="64" viewBox="0 0 72 64">
      <path d="M36 2C56 2 70 13 70 28C70 43 56 53 44 53L44 63C38 60 30 56 22 52C10 48 2 40 2 28C2 13 16 2 36 2Z" fill="var(--accent)"/>
      <circle cx="22" cy="28" r="4.5" fill="#d9d9d9"/>
      <circle cx="36" cy="28" r="4.5" fill="#d9d9d9"/>
      <circle cx="50" cy="28" r="4.5" fill="#d9d9d9"/>
    </svg>
  </div>

  <div class="card small" style="left:22px">
    <div class="card-label">Beratung</div>
    <svg width="50" height="48" viewBox="0 0 50 48">
      <path d="M4 14C2 8 5 4 10 4L14 14L10 19C13 27 19 33 27 37L32 32L42 37C42 43 38 46 32 45C18 41 8 30 4 14Z" fill="var(--accent)"/>
      <circle cx="37" cy="12" r="11" fill="var(--accent)"/>
      <path d="M37 6V18M31 12H43" stroke="#d9d9d9" stroke-width="3"/>
    </svg>
  </div>

  <div class="card small" style="left:217px">
    <div class="card-label">Management</div>
    <svg width="50" height="54" viewBox="0 0 50 54">
      <rect x="2" y="2" width="22" height="46" rx="2" fill="var(--accent)"/>
      <rect x="27" y="2" width="21" height="46" rx="2" fill="var(--accent)"/>
      <path d="M10 46V53L14 50L18 53V46Z M32 46V53L36 50L40 53V46Z" fill="var(--accent)"/>
      <g fill="#d9d9d9">
        <rect x="8" y="10" width="4" height="4"/><rect x="8" y="20" width="4" height="4"/><rect x="8" y="30" width="4" height="4"/>
        <rect x="35" y="10" width="4" height="4"/><rect x="35" y="20" width="4" height="4"/><rect x="35" y="30" width="4" height="4"/>
      </g>
    </svg>
  </div>

  <div class="card small" style="left:413px">
    <div class="card-label">Projekte aller Art</div>
    <svg width="46" height="52" viewBox="0 0 46 52">
      <rect x="2" y="7" width="42" height="44" rx="3" fill="var(--accent)"/>
      <rect x="15" y="2" width="16" height="10" rx="3" fill="var(--accent)" stroke="#d9d9d9" stroke-width="2"/>
      <path d="M8 34L17 25L24 31L36 19" stroke="#d9d9d9" stroke-width="3" fill="none"/>
      <rect x="8" y="41" width="30" height="3" fill="#d9d9d9"/>
    </svg>
  </div>

  <p class="motto">Mit Präzision und langjähriger Erfahrung<br>immer alles im Griff!</p>

  <div class="contact">
    <p>Gerne schicke ich Ihnen unverbindlich mein Expertenprofil samt CV sowie meine aktuellen Verfügbarkeiten zu.</p>
    <p>Kontaktieren Sie mich hierzu einfach per E-Mail unter <strong>m punkt berger at wolkentor-web punkt de.</strong> Ich freue mich auf Sie!</p>
  </div>
  <a class="legal" href="#impressum">[ Impressum / Datenschutzerklärung ]</a>
</body>
</html>
```